Food Festival "Signature Cocktail" Booth Banner

Need a 3'x9'6" (36" tall x 114" wide) Outdoor Banner for a new "Signature Cocktail" booth at an outdoor food festival. Marlowe Onion Jubilee is a non profit festival and the World Record largest Garlic Festival with average of 100K attendees over 3 days. Actual drink served will vary from year to year, but banner for the booth with be reused each year so it will be non drink specific. Banner needs to catch attendee's attention both at a quick glance and from a distance outdoors to drive traffic and sales to the booth. It will be mounted above the sales window of a 10x10 Festival Booth on PVC frame (see attached pic for reference). "Signature Cocktail" is required text along with it being identified as a Marlowe Onion Jubilee booth either through use of attached logo (color can be modified) or "Marlowe Onion Jubilee" text since we also have for profit competing vendors. Banner will be full color print. Idea concepts: Neon Sign, Art Deco elegant, reclaimed wood...but open to any concepts. Festival website: https://marloweonionjubilee.example

Target Market(s)

Food Festival Attendees

Font styles to use
Decorative
Script
Other font styles liked:
• Neon, heavy weight fonts, open.

Colors

Designer to choose colors to be used in the design.

Requirements
Must have
• "Signature Cocktail" and "Marlowe Onion Jubilee" text or MOJ Logo provided, colors and layout that stands out and easily identifiable and readable from a long distance with strong text
Nice to have
• Vibrant engaging background,, ties to Garlic
Should not have
• Clip art, generic text

```html
<!DOCTYPE html>
<html lang="en">
<head>
<meta charset="utf-8">
<title>Marlowe Onion Jubilee – Signature Cocktail Booth Banner</title>
<link href="https://fonts.googleapis.com/css2?family=Luckiest+Guy&display=swap" rel="stylesheet">
<style>
  :root {
    --banner-center: #992a5e;
    --banner-edge: #471a4c;
    --brand-white: #ffffff;
    --headline-top: #ffe600;
    --headline-bottom: #f36f1c;
    --headline-shadow: #ffffff;
  }
  html, body {
    margin: 0;
    padding: 0;
    width: 1200px;
    height: 470px;
    overflow: hidden;
    background: var(--banner-edge);
  }
  .banner {
    position: relative;
    width: 1200px;
    height: 470px;
    background: radial-gradient(ellipse 70% 90% at 55% 50%, var(--banner-center) 0%, #7d2358 45%, var(--banner-edge) 100%);
    overflow: hidden;
  }
  .festival-mark {
    position: absolute;
    left: 40px;
    top: 85px;
    width: 300px;
    height: 300px;
  }
  .festival-mark__ring {
    position: absolute;
    inset: 0;
    border: 6px solid var(--brand-white);
    border-radius: 50%;
    box-sizing: border-box;
  }
  .festival-mark__name {
    position: absolute;
    inset: 0;
    display: flex;
    flex-direction: column;
    align-items: center;
    justify-content: center;
    margin: 0;
    font-family: "Luckiest Guy", system-ui, sans-serif;
    font-weight: 400;
    font-size: 46px;
    line-height: 1.05;
    color: var(--brand-white);
    text-align: center;
    letter-spacing: 1px;
  }
  .headline {
    position: absolute;
    left: 380px;
    top: 60px;
    width: 760px;
    height: 370px;
  }
  .headline text {
    font-family: "Luckiest Guy", system-ui, sans-serif;
  }
</style>
</head>
<body>
  <main class="banner">
    <div class="festival-mark">
      <div class="festival-mark__ring"></div>
      <h2 class="festival-mark__name"><span>Marlowe</span><span>Onion</span><span>Jubilee</span></h2>
    </div>

    <svg class="headline" viewBox="0 0 760 370" role="img" aria-label="Signature Cocktail">
      <defs>
        <linearGradient id="headline-fill" x1="0" y1="0" x2="0" y2="1">
          <stop offset="0" stop-color="var(--headline-top)"/>
          <stop offset="1" stop-color="var(--headline-bottom)"/>
        </linearGradient>
      </defs>

      <g class="headline__shadow" fill="var(--headline-shadow)" transform="translate(8,7)">
        <text x="0" y="165"><tspan font-size="170">SIGN</tspan><tspan font-size="125">ATU</tspan><tspan font-size="72" dy="-40">RE</tspan></text>
        <text x="0" y="345"><tspan font-size="170">COCK</tspan><tspan font-size="125">TAIL</tspan></text>
      </g>

      <g class="headline__face" fill="url(#headline-fill)">
        <text x="0" y="165"><tspan font-size="170">SIGN</tspan><tspan font-size="125">ATU</tspan><tspan font-size="72" dy="-40">RE</tspan></text>
        <text x="0" y="345"><tspan font-size="170">COCK</tspan><tspan font-size="125">TAIL</tspan></text>
      </g>
    </svg>
  </main>
</body>
</html>
```